Window and GutterCleaning Flyer A5 size double sided.

We need a double sided A5 flyer. Side 1, is for window cleaning, side 2 is for gutter cleaning. Licensed by Borough of Halvern Council.
Phone number 0800 315 4720.
Business address 7 Tarnlow Brae, North Pellin Edinburgh EH14 3RW.
www.clearpane-vista-services.com
We use a LoftPro Gutter inspection Cam to view your gutters first to see if they need doing.
Window cleaning ; Professional window cleaning services, what we offer, water fed pole window cleaning able to reach windows up to 60 feet.
Conservatory cleaning.
Conservatory roof cleaning.
Fascias & Soffits cleaning.
Excellent Customer Service.
Target Market(s)
domestic houses
Industry/Entity Type
window cleaning
Look and feel
Each slider illustrates characteristics of the customer's brand and the style your logo design should communicate.

```html
<!DOCTYPE html>
<html lang="en">
<head>
<meta charset="utf-8">
<title>ClearPane Vista – Window &amp; Gutter Flyers</title>
<link href="https://fonts.googleapis.com/css2?family=Poppins:wght@400;500;600;700;800&family=Oswald:wght@500;600&display=swap" rel="stylesheet">
<style>
:root{
  --navy:#2d2660;
  --navy-soft:#3b3480;
  --tile:#5d68a8;
  --sky:#64abe9;
  --sky-pale:#9ecbf2;
  --ink:#1d1d2b;
  --page:#ffffff;
  --stage:#c7c7c7;
  --rule:#b9b9c4;
}
*{box-sizing:border-box;margin:0;padding:0}
html,body{width:1200px;height:1200px;overflow:hidden;background:var(--stage);font-family:"Poppins",sans-serif;color:var(--ink)}
.flyer{position:absolute;top:230px;width:521px;height:739px;background:var(--page);overflow:hidden}
.flyer--windows{left:55px}
.flyer--gutters{left:618px}
.abs{position:absolute}
.brand{text-align:center;width:120px}
.brand__roof{display:block;margin:0 auto 2px}
.brand__name{font-weight:700;font-size:24px;color:var(--navy);line-height:1}
.brand__tag{margin-top:3px;background:var(--sky-pale);font-size:6.5px;font-weight:600;color:var(--navy);line-height:1.25;padding:2px 0;letter-spacing:.2px}
.photo{background:linear-gradient(160deg,#d4e6f5,#8fb6d6 60%,#6e93b6);border-radius:3px}
.photo--framed{border:3px solid #fff;box-shadow:0 1px 4px rgba(0,0,0,.35)}
.band{position:absolute;left:0;width:521px;background:var(--navy)}
.band__wave{position:absolute;left:0;top:-14px;width:521px;height:16px}
.offer-title{position:absolute;color:#fff;font-weight:700;font-size:20px;letter-spacing:.8px;display:flex;align-items:center;gap:8px}
.offer-title i{display:block;height:1px;background:#9a9ac2}
.tile{position:absolute;height:35px;border-radius:4px;display:flex;align-items:center;padding-left:14px;color:#fff;font-size:8.6px;line-height:1.2;font-weight:500}
.tile--light{background:var(--tile)}
.tile--dark{background:var(--navy-soft)}
.tile__icon{position:absolute;left:-9px;top:7px;width:21px;height:21px;border-radius:50%;background:#fff;border:2px solid var(--sky-pale);display:flex;align-items:center;justify-content:center}
.badge-plain{display:inline-block;width:84px;height:11px;border-radius:2px;background:#cfd2ea;margin-top:2px}
.footer{position:absolute;top:688px;font-size:10px;line-height:1.25;color:var(--ink)}
.footer b{color:var(--navy);font-weight:700}
.pill{position:absolute;height:19px;border-radius:10px;background:var(--navy);color:#fff;font-size:10px;display:flex;align-items:center;justify-content:center}
.arrow{position:absolute}
.arrow span{position:absolute;left:0;right:14px;top:0;bottom:0;display:flex;align-items:center;justify-content:center;color:#fff;font-weight:600;font-size:19px}
</style>
</head>
<body>

<!-- Side 1: window cleaning -->
<section class="flyer flyer--windows">
  <div class="photo abs" style="left:279px;top:0;width:242px;height:310px" role="img" aria-label="Rope access cleaner washing a tall glass building facade"></div>

  <div class="brand abs" style="left:82px;top:20px">
    <svg class="brand__roof" width="70" height="20" viewBox="0 0 70 20"><rect x="29" y="6" width="12" height="12" fill="#fff" stroke="#2d2660" stroke-width="2.5"/></svg>
    <div class="brand__name">CPV</div>
    <div class="brand__tag">CLEARPANE VISTA<br>Edinburgh</div>
  </div>

  <div class="abs" style="left:0;width:283px;top:99px;text-align:center">
    <div style="font-size:18.5px;letter-spacing:.6px;line-height:1.1">Let the Sunshine In</div>
    <div style="font-size:25px;font-weight:600;line-height:1.1;margin-top:1px">Sparkling <span style="color:var(--sky)">✦</span></div>
    <div style="font-size:37px;font-weight:800;color:var(--navy);line-height:1.02;margin-top:2px">Windows</div>
    <div style="font-size:33px;font-weight:800;color:var(--sky);line-height:1">Guaranteed</div>
    <p style="font-size:10.4px;line-height:1.22;margin:8px 20px 0 26px">We offer high-quality window cleaning for homes and businesses, delivering. We only clean domestic properties not businesses. Spotless, streak-free results every time. As per last info, can't claim this too.</p>
  </div>

  <div class="band" style="top:306px;height:146px">
    <svg class="band__wave" viewBox="0 0 521 16" preserveAspectRatio="none"><path d="M0 10 Q60 2 130 8 T260 6 T400 4 T521 2 V16 H0Z" fill="#2d2660"/></svg>
    <div class="offer-title" style="left:80px;top:13px"><i style="width:122px"></i>WE OFFER<i style="width:122px"></i></div>
    <div class="tile tile--dark" style="left:40px;top:45px;width:136px">Water-Fed Pole Cleaning<br>– Up to 60 Feet<span class="tile__icon"><svg width="10" height="10"><path d="M2 8 L8 2" stroke="#2d2660" stroke-width="1.5"/></svg></span></div>
    <div class="tile tile--light" style="left:200px;top:45px;width:136px">Fascia &amp; Soffit Cleaning<span class="tile__icon"><svg width="10" height="10"><rect x="1.5" y="2" width="7" height="6" fill="none" stroke="#2d2660" stroke-width="1.2"/></svg></span></div>
    <div class="tile tile--dark" style="left:357px;top:45px;width:136px">Reliable, Friendly Service<span class="tile__icon"><svg width="10" height="10"><circle cx="5" cy="5" r="3.5" fill="none" stroke="#2d2660" stroke-width="1.2"/></svg></span></div>
    <div class="tile tile--light" style="left:40px;top:90px;width:136px">Conservatory<br>Windows &amp; Roofs<span class="tile__icon"><svg width="10" height="10"><rect x="2" y="1.5" width="6" height="7" fill="none" stroke="#2d2660" stroke-width="1.2"/><path d="M5 1.5V8.5" stroke="#2d2660"/></svg></span></div>
    <div class="tile tile--dark" style="left:200px;top:90px;width:136px">One-off or Regular<br>Cleans<span class="tile__icon"><svg width="10" height="10"><path d="M5 1 L6 4 L9 5 L6 6 L5 9 L4 6 L1 5 L4 4Z" fill="#2d2660"/></svg></span></div>
    <div class="tile tile--light" style="left:357px;top:90px;width:136px;flex-direction:column;align-items:flex-start;justify-content:center">Licensed by<span class="badge-plain"></span><span class="tile__icon"><svg width="10" height="10"><rect x="1.5" y="1.5" width="7" height="7" fill="none" stroke="#2d2660" stroke-width="1.2"/></svg></span></div>
  </div>

  <div class="photo photo--framed abs" style="left:33px;top:472px;width:111px;height:183px;background:linear-gradient(170deg,#7ea0c8,#5c7fae 55%,#a9c2de)" role="img" aria-label="Squeegee wiping a wet window pane"></div>
  <div class="photo photo--framed abs" style="left:155px;top:472px;width:108px;height:86px;background:linear-gradient(135deg,#a05a40,#c9b7a6 60%,#8f5a43)" role="img" aria-label="Water-fed pole cleaning a brick house window"></div>
  <div class="photo photo--framed abs" style="left:155px;top:569px;width:108px;height:86px;background:linear-gradient(135deg,#e5ece9,#7b8a80 60%,#d9e3e0)" role="img" aria-label="Pole brush scrubbing a white window frame"></div>

  <div class="abs" style="left:288px;top:470px;width:220px">
    <div style="font-size:18.5px;font-weight:600;line-height:1.15;color:#2a2a33">GREAT SERVICE FROM</div>
    <div style="font-size:18.5px;font-weight:700;line-height:1.15;color:var(--navy)">START TO FINISH</div>
    <div style="font-size:14.4px;font-weight:600;line-height:1.25;margin-top:8px">Reliable, professional and the windows have never looked better!</div>
    <div style="height:1px;background:var(--rule);margin-top:13px;width:197px"></div>
    <div style="font-size:17.5px;margin-top:12px">BASED IN <b style="color:var(--navy);font-weight:700">NORTH PELLIN</b></div>
    <div style="margin-top:4px;width:199px;height:35px;border-radius:4px;background:var(--sky-pale);display:flex;align-items:center;justify-content:center;font-size:16px;color:var(--navy)">Serving All of Edinburgh</div>
  </div>

  <div class="footer" style="left:33px">Get a <b>FREE QUOTE</b><br><svg width="8" height="8" viewBox="0 0 10 10"><path d="M2 1 L4 1 L5 3 L4 4 Q5 6 6 6 L7 5 L9 6 L9 8 Q6 9 3 6 Q1 3 2 1Z" fill="#2d2660"/></svg> 0800 315 4720</div>
  <div class="footer" style="left:148px;width:140px"><svg width="8" height="10" viewBox="0 0 8 10"><path d="M4 10 L1 5 A3 3 0 1 1 7 5Z" fill="#2d2660"/><circle cx="4" cy="3.5" r="1.2" fill="#fff"/></svg> 7 Tarnlow Brae, North Pellin, Edinburgh EH14 3RW</div>
  <div class="pill" style="left:300px;top:688px;width:196px;font-size:9px">www.clearpane-vista-services.com</div>
</section>

<!-- Side 2: gutter cleaning -->
<section class="flyer flyer--gutters">
  <div class="photo abs" style="left:270px;top:37px;width:251px;height:250px;clip-path:polygon(100% 0,100% 100%,0 100%,0 95%);background:linear-gradient(200deg,#e9ecef,#bfc6cc 45%,#9b5d46 75%,#7a4a3a)" role="img" aria-label="House roofline showing gutter, fascia and soffit"></div>

  <div class="arrow" style="left:358px;top:55px;width:128px;height:50px"><svg width="128" height="50"><path d="M0 6 H100 L96 0 L126 25 L96 50 L100 44 H0 L10 25Z" fill="#2d2660"/></svg><span>Gutter</span></div>
  <div class="arrow" style="left:318px;top:126px;width:130px;height:50px"><svg width="130" height="50"><path d="M0 6 H102 L98 0 L128 25 L98 50 L102 44 H0 L10 25Z" fill="#64abe9"/></svg><span>Fascia</span></div>
  <div class="arrow" style="left:278px;top:196px;width:130px;height:50px"><svg width="130" height="50"><path d="M0 6 H102 L98 0 L128 25 L98 50 L102 44 H0 L10 25Z" fill="#2d2660"/></svg><span>Soffit</span></div>

  <div class="brand abs" style="left:100px;top:20px">
    <svg class="brand__roof" width="70" height="20" viewBox="0 0 70 20"><rect x="29" y="6" width="12" height="12" fill="#fff" stroke="#2d2660" stroke-width="2.5"/></svg>
    <div class="brand__name">CPV</div>
    <div class="brand__tag">CLEARPANE VISTA<br>Edinburgh</div>
  </div>

  <div class="abs" style="left:30px;top:110px;width:270px">
    <div style="font-size:23px;letter-spacing:.6px;line-height:1.05">Don't Let Blocked</div>
    <div style="font-size:31px;font-weight:700;color:var(--sky);line-height:1">Gutters Cause</div>
    <div style="font-size:31px;font-weight:700;color:var(--navy);line-height:1.05">Costly Damage</div>
    <div style="font-size:17.5px;font-weight:500;line-height:1.22;margin-top:6px">We inspect before<br>we clean saving you time<br>and money.</div>
  </div>

  <div class="band" style="top:278px;height:160px">
    <svg class="band__wave" viewBox="0 0 521 16" preserveAspectRatio="none"><path d="M0 12 Q80 4 160 8 T300 4 T420 8 T521 6 V16 H0Z" fill="#2d2660"/></svg>
    <div class="abs" style="left:35px;top:24px;width:127px;height:113px;border-radius:6px;background:#1f7ad0;padding:3px">
      <div style="height:100%;border:1px dashed #cfe6fa;border-radius:4px;text-align:center;color:#fff;overflow:hidden">
        <div style="font-family:'Oswald',sans-serif;font-weight:600;font-size:14.5px;margin-top:6px;line-height:1.1">FREE GUTTER CHECK</div>
        <div style="font-size:11px;line-height:1.15">with LoftPro<br>Inspection Cam</div>
        <div style="background:var(--sky-pale);color:var(--navy);font-size:7px;line-height:1.25;padding:6px 6px;margin-top:8px;height:46px">We show you what's really going on before recommending service.</div>
      </div>
    </div>
    <div class="offer-title" style="left:181px;top:22px">WE OFFER<i style="width:122px"></i></div>
    <div class="tile tile--dark" style="left:187px;top:55px;width:134px">Safe, No-Ladder<br>Cleaning<span class="tile__icon"><svg width="10" height="10"><path d="M5 1 L9 2.5 V5 Q9 8 5 9 Q1 8 1 5 V2.5Z" fill="none" stroke="#2d2660" stroke-width="1.1"/></svg></span></div>
    <div class="tile tile--light" style="left:347px;top:55px;width:134px">Prevents Overflow, Damp<br>&amp; Water Damage<span class="tile__icon"><svg width="10" height="10"><path d="M1 5 L5 1.5 L9 5 M2.5 4 V8.5 H7.5 V4" fill="none" stroke="#2d2660" stroke-width="1.1"/></svg></span></div>
    <div class="tile tile--light" style="left:187px;top:101px;width:134px">Removes Moss, Leaves<br>&amp; Debris<span class="tile__icon"><svg width="10" height="10"><rect x="2" y="3" width="6" height="6" fill="none" stroke="#2d2660" stroke-width="1.1"/><path d="M1 3 H9" stroke="#2d2660"/></svg></span></div>
    <div class="tile tile--dark" style="left:347px;top:101px;width:134px">Fast, Clean &amp; Fully<br>Insured<span class="tile__icon"><svg width="10" height="10"><path d="M5 1 L6 4 L9 5 L6 6 L5 9 L4 6 L1 5 L4 4Z" fill="#2d2660"/></svg></span></div>
  </div>

  <div class="photo photo--framed abs" style="left:32px;top:462px;width:109px;height:89px;background:linear-gradient(180deg,#c9d6e2,#9a6c58 45%,#d8d2c8)" role="img" aria-label="Cleaner beside a conservatory at a brick house"></div>
  <div class="photo photo--framed abs" style="left:152px;top:462px;width:109px;height:89px;background:linear-gradient(135deg,#7d8a7a,#e7e9ea 50%,#3c46a0)" role="img" aria-label="Vacuum hose clearing a gutter"></div>
  <div class="photo photo--framed abs" style="left:32px;top:563px;width:109px;height:89px;background:linear-gradient(180deg,#d9dcdf,#7d7a5c 45%,#d6dadc)" role="img" aria-label="Mossy conservatory roof before cleaning"></div>
  <div class="photo photo--framed abs" style="left:152px;top:563px;width:109px;height:89px;background:linear-gradient(160deg,#8fae6c,#5c7a46 50%,#9aa3a8)" role="img" aria-label="Inspection pole camera over a gutter"></div>

  <div class="abs" style="left:282px;top:460px;width:220px">
    <div style="font-size:17px;font-weight:700;color:var(--navy);line-height:1.2">WHY CHOOSE US?</div>
    <ul style="list-style:none;font-size:11.6px;line-height:1.05;margin-top:7px">
      <li style="display:flex;gap:8px;margin-bottom:11px"><svg width="11" height="11" viewBox="0 0 10 10"><path d="M1 5 L5 1.5 L9 5 M2.5 4 V8.5 H7.5 V4" fill="none" stroke="#2d2660" stroke-width="1.2"/><path d="M3.6 6 L4.8 7.2 L6.8 5" fill="none" stroke="#64abe9" stroke-width="1"/></svg><span>Friendly, professional<br>service</span></li>
      <li style="display:flex;gap:8px;margin-bottom:11px"><svg width="11" height="11" viewBox="0 0 10 10"><path d="M1 5 L5 1.5 L9 5 M2.5 4 V8.5 H7.5 V4" fill="none" stroke="#2d2660" stroke-width="1.2"/><path d="M3.6 6 L4.8 7.2 L6.8 5" fill="none" stroke="#64abe9" stroke-width="1"/></svg><span>Reliable and efficient</span></li>
      <li style="display:flex;gap:8px;margin-bottom:11px"><svg width="11" height="11" viewBox="0 0 10 10"><path d="M1 5 L5 1.5 L9 5 M2.5 4 V8.5 H7.5 V4" fill="none" stroke="#2d2660" stroke-width="1.2"/><path d="M3.6 6 L4.8 7.2 L6.8 5" fill="none" stroke="#64abe9" stroke-width="1"/></svg><span>Fully licensed and insured</span></li>
      <li style="display:flex;gap:8px"><svg width="11" height="11" viewBox="0 0 10 10"><path d="M1 5 L5 1.5 L9 5 M2.5 4 V8.5 H7.5 V4" fill="none" stroke="#2d2660" stroke-width="1.2"/><path d="M3.6 6 L4.8 7.2 L6.8 5" fill="none" stroke="#64abe9" stroke-width="1"/></svg><span>Excellent customer<br>satisfaction</span></li>
    </ul>
    <div style="height:1px;background:var(--rule);margin-top:12px;width:196px"></div>
    <div style="font-size:14px;margin-top:10px">Stay Ahead of Leaks</div>
    <div style="display:flex;align-items:center;gap:5px;margin-top:1px">
      <span style="font-size:31px;font-weight:800;color:var(--navy);line-height:1">BOOK</span>
      <span style="font-size:12.5px;font-weight:700;color:var(--navy);line-height:1.05">Your Gutter<br>Check Today!</span>
    </div>
  </div>

  <div class="footer" style="left:33px">Get a <b>FREE QUOTE</b><br><svg width="8" height="8" viewBox="0 0 10 10"><path d="M2 1 L4 1 L5 3 L4 4 Q5 6 6 6 L7 5 L9 6 L9 8 Q6 9 3 6 Q1 3 2 1Z" fill="#2d2660"/></svg> 0800 315 4720</div>
  <div class="pill" style="left:142px;top:688px;width:195px;font-size:8.8px">www.clearpane-vista-services.com</div>
  <div class="pill" style="left:342px;top:689px;width:68px;height:17px;background:var(--sky-pale);color:var(--navy);font-size:8.5px">Licensed by</div>
  <div class="abs" style="left:418px;top:685px;width:64px;text-align:center">
    <div style="width:56px;height:10px;background:#d7d9e6;border-radius:2px;margin:0 auto"></div>
    <div style="font-size:6px;margin-top:3px;color:var(--ink)">AFFORDABLE | LOCAL</div>
  </div>
</section>

</body>
</html>
```